Etiketten für Olivenöl
Zielgruppe
Handel mit Oliven und Olivenölen unsere Zielgruppe sind qualitativ anspruchsvolle Menschen.
Aufgabenstellung
Wir benötigen ein Produktetikett für eine Olivenöl Flasche Form Nerella 250ml und 500ml mit Vorder- und Rückseite Lg. 14cm und Br. 5cm für 250 ml Flasche und Lg. 18cm und Br. 7cm für 500ml Flasche.
Das Etikett kann gern einen matten Hintergrund haben oder auch ganz durchsichtig sein.
Der Name Velmira bedeutet Olivenbaum und sollte berücksichtigt werden.
Folgende Angaben bzw. Felder muss das Etikett beinhalten:
Barcode, Inhaltsstoffe, Haltbarkeitsdatum, Artikelnummer

```html
<!DOCTYPE html>
<html lang="de">
<head>
<meta charset="utf-8">
<title>Velmira – Olivenöl Etiketten</title>
<link href="https://fonts.googleapis.com/css2?family=Bitter:wght@500;600;700&family=Barlow+Condensed:wght@400;500&family=Josefin+Sans:wght@300;400;600&display=swap" rel="stylesheet">
<style>
  :root {
    --page: #f4f4f4;
    --label: #38383a;
    --accent: #e8a466;
    --branch: #5f7a66;
    --white: #ffffff;
    --ink: #1e1e1e;
  }
  * { margin: 0; padding: 0; box-sizing: border-box; }
  html, body { width: 1200px; height: 3085px; overflow: hidden; background: var(--page); }
  .sheet { position: relative; width: 1200px; height: 3085px; }

  .label {
    position: absolute;
    width: 448px;
    height: 1814px;
    background: var(--label);
    border-radius: 224px 224px 28px 28px;
    overflow: hidden;
    color: var(--accent);
    text-align: center;
  }
  .label > * { position: absolute; left: 0; right: 0; }

  .branch-art {
    background:
      radial-gradient(ellipse 40% 30% at 50% 45%, rgba(95,122,102,0.28), transparent 70%),
      linear-gradient(200deg, transparent 10%, rgba(95,122,102,0.18) 45%, rgba(95,122,102,0.10) 80%, transparent);
  }

  .brand-mark {
    left: 50%; right: auto;
    width: 110px; height: 110px;
    margin-left: -55px;
    border: 3px solid var(--accent);
    border-radius: 50%;
  }
  .brand-name {
    font-family: "Bitter", serif;
    font-weight: 600;
    font-size: 34px;
    letter-spacing: 3px;
    line-height: 34px;
  }

  .grade {
    font-family: "Bitter", serif;
    font-weight: 600;
    font-size: 40px;
    line-height: 55px;
    letter-spacing: 2px;
  }
  .product-name {
    font-family: "Bitter", serif;
    font-weight: 700;
    line-height: 1;
  }
  .product-name .word-oliven { display: block; font-size: 132px; letter-spacing: -3px; }
  .product-name .word-oel { display: block; font-size: 224px; letter-spacing: -8px; margin-top: -8px; }
  .subline {
    font-family: "Bitter", serif;
    font-weight: 600;
    font-size: 31px;
    line-height: 42px;
    letter-spacing: 2px;
  }
  .volume {
    font-family: "Josefin Sans", sans-serif;
    font-weight: 600;
    font-size: 38px;
    letter-spacing: 9px;
    line-height: 38px;
  }

  .info {
    font-family: "Bitter", serif;
    font-weight: 600;
    font-size: 24px;
    line-height: 32px;
    letter-spacing: 1.5px;
  }
  .nutrition {
    left: 63px; right: auto;
    width: 333px;
    height: 383px;
    border: 2px solid var(--accent);
    padding: 10px 18px 0;
    font-family: "Barlow Condensed", sans-serif;
    font-size: 24px;
    text-align: left;
  }
  .nutrition .row { display: flex; justify-content: space-between; height: 33px; line-height: 33px; }
  .nutrition .group { margin-top: 32px; }
  .nutrition .head { font-weight: 500; }
  .contact, .best-before {
    font-family: "Josefin Sans", sans-serif;
    font-weight: 300;
    font-size: 21px;
    line-height: 27px;
    letter-spacing: 2px;
  }
  .barcode-field {
    left: 38px; right: auto;
    width: 371px;
    height: 260px;
    background: var(--white);
    color: var(--ink);
    font-family: "Josefin Sans", sans-serif;
    font-weight: 600;
    font-size: 25px;
    letter-spacing: 1px;
    display: flex; align-items: center; justify-content: center;
  }

  .mini { position: absolute; transform-origin: top left; }
  .mini .label { position: relative; }
</style>
</head>
<body>
<main class="sheet">

  <!-- Front label 250 ml -->
  <section class="label label-front" style="left:77px; top:36px;">
    <div class="branch-art" role="img" aria-label="Olivenzweig mit Blättern und Oliven als feine grüne Linienzeichnung" style="top:430px; height:1384px;"></div>
    <div class="brand-mark" style="top:170px;"></div>
    <div class="brand-name" style="top:347px;">VELMIRA</div>
    <div class="grade" style="top:625px;">EXTRA<br>NATIVES</div>
    <div class="product-name" style="top:822px;"><span class="word-oliven">Oliven</span><span class="word-oel">Öl</span></div>
    <div class="subline" style="top:1243px;">ACEITE DE OLIVA<br>PREMIUM QUALITY</div>
    <div class="volume" style="top:1670px;">250ML</div>
  </section>

  <!-- Back label -->
  <section class="label label-back" style="left:676px; top:36px;">
    <div class="branch-art" role="img" aria-label="Olivenzweig als feine grüne Linienzeichnung" style="top:740px; height:840px;"></div>
    <div class="brand-mark" style="top:170px;"></div>
    <div class="brand-name" style="top:347px;">VELMIRA</div>
    <div class="info" style="top:509px;">ZUTATEN:<br>100% NATIVES OLIVENÖL</div>
    <div class="info" style="top:653px;">VOR WÄRME UND LICHT<br>GESCHÜTZT LAGERN.</div>
    <div class="nutrition" style="top:775px;">
      <div class="row head"><span>Nährwertangabe pro 100ml</span></div>
      <div class="row"><span>Energie</span><span>25,6 kcal / 107,4 KJ</span></div>
      <div class="row group"><span>Fett</span><span>0,0 g</span></div>
      <div class="row"><span>davon ges. Fettsäuren</span><span>0,0 g</span></div>
      <div class="row group"><span>Kohlenhydrate</span><span>6,2 g</span></div>
      <div class="row"><span>davon Zucker</span><span>6,2 g</span></div>
      <div class="row group"><span>Eiweiss</span><span>0,1 g</span></div>
      <div class="row"><span>Salz</span><span>0,0 g</span></div>
    </div>
    <div class="contact" style="top:1217px;">VELMIRA<br>MUSTERSTR. 11<br>12345 MUSTERSTADT<br>WWW.VELMIRA.DE</div>
    <div class="best-before" style="top:1409px;">UNGEÖFFNET MINDESTENS<br>HALTBAR BIS:</div>
    <div class="barcode-field" style="top:1570px;">BARCODE</div>
  </section>

  <!-- Small front 250 ml -->
  <div class="mini" style="left:131px; top:2322px; transform:scale(0.324);">
    <section class="label label-front">
      <div class="branch-art" role="img" aria-label="Olivenzweig als Linienzeichnung" style="top:430px; height:1384px;"></div>
      <div class="brand-mark" style="top:170px;"></div>
      <div class="brand-name" style="top:347px;">VELMIRA</div>
      <div class="grade" style="top:625px;">EXTRA<br>NATIVES</div>
      <div class="product-name" style="top:822px;"><span class="word-oliven">Oliven</span><span class="word-oel">Öl</span></div>
      <div class="subline" style="top:1243px;">ACEITE DE OLIVA<br>PREMIUM QUALITY</div>
      <div class="volume" style="top:1670px;">250ML</div>
    </section>
  </div>

  <!-- Small back 250 ml -->
  <div class="mini" style="left:453px; top:2322px; transform:scale(0.324);">
    <section class="label label-back">
      <div class="branch-art" role="img" aria-label="Olivenzweig als Linienzeichnung" style="top:740px; height:840px;"></div>
      <div class="brand-mark" style="top:170px;"></div>
      <div class="brand-name" style="top:347px;">VELMIRA</div>
      <div class="info" style="top:509px;">ZUTATEN:<br>100% NATIVES OLIVENÖL</div>
      <div class="info" style="top:653px;">VOR WÄRME UND LICHT<br>GESCHÜTZT LAGERN.</div>
      <div class="nutrition" style="top:775px;">
        <div class="row head"><span>Nährwertangabe pro 100ml</span></div>
        <div class="row"><span>Energie</span><span>25,6 kcal / 107,4 KJ</span></div>
        <div class="row group"><span>Fett</span><span>0,0 g</span></div>
        <div class="row"><span>davon ges. Fettsäuren</span><span>0,0 g</span></div>
        <div class="row group"><span>Kohlenhydrate</span><span>6,2 g</span></div>
        <div class="row"><span>davon Zucker</span><span>6,2 g</span></div>
        <div class="row group"><span>Eiweiss</span><span>0,1 g</span></div>
        <div class="row"><span>Salz</span><span>0,0 g</span></div>
      </div>
      <div class="contact" style="top:1217px;">VELMIRA<br>MUSTERSTR. 11<br>12345 MUSTERSTADT<br>WWW.VELMIRA.DE</div>
      <div class="best-before" style="top:1409px;">UNGEÖFFNET MINDESTENS<br>HALTBAR BIS:</div>
      <div class="barcode-field" style="top:1570px;">BARCODE</div>
    </section>
  </div>

  <!-- Small front 500 ml -->
  <div class="mini" style="left:875px; top:2191px; transform:scale(0.401);">
    <section class="label label-front">
      <div class="branch-art" role="img" aria-label="Olivenzweig als Linienzeichnung" style="top:430px; height:1384px;"></div>
      <div class="brand-mark" style="top:170px;"></div>
      <div class="brand-name" style="top:347px;">VELMIRA</div>
      <div class="grade" style="top:625px;">EXTRA<br>NATIVES</div>
      <div class="product-name" style="top:822px;"><span class="word-oliven">Oliven</span><span class="word-oel">Öl</span></div>
      <div class="subline" style="top:1243px;">ACEITE DE OLIVA<br>PREMIUM QUALITY</div>
      <div class="volume" style="top:1670px;">500ML</div>
    </section>
  </div>

</main>
</body>
</html>
```